Business Card/Letterhead Design

We have our Logo, we simply need it cleaned up. Along with a letterhead design. It's pretty simple really.
Instead of the "Corporation" beside the logo. We need it to say "Limited" just under the logo between the "F" and the "Y"
The letter head has to have our address. 4375 Calverton Road Mississauga, ON L4W 2K7 Canada
Updates
Reason: I have been called out of town until Monday of next week.
Industry/Entity Type
Business
Contact Information for Business Card
4375 Calverton Road Mississauga, ON L4W 2K7 Canada
Look and feel
Each slider illustrates characteristics of the customer's brand and the style your logo design should communicate.

```html
<!DOCTYPE html>
<html lang="en">
<head>
<meta charset="utf-8">
<title>Northgate Limited — Business Card</title>
<link rel="stylesheet" href="https://fonts.googleapis.com/css2?family=Cinzel:wght@400;600&display=swap">
<style>
  :root {
    --page-bg: #2a2a2c;
    --band-blue: #3438a8;
    --band-blue-dark: #26298a;
    --rule-white: #f2f2f4;
    --silver-light: #e6e6e8;
    --silver-mid: #c4c4c7;
    --silver-dark: #9d9da1;
    --ink-blue: #2e3193;
    --address-white: #ffffff;
  }
  * { margin: 0; padding: 0; box-sizing: border-box; }
  html, body {
    width: 1200px;
    height: 960px;
    overflow: hidden;
    background: var(--page-bg);
  }
  .canvas {
    position: relative;
    width: 1200px;
    height: 960px;
    display: flex;
    align-items: center;
    justify-content: center;
  }
  .business-card {
    position: relative;
    width: 900px;
    height: 540px;
    border-radius: 34px;
    overflow: hidden;
    background: linear-gradient(100deg,
      var(--silver-dark) 0%,
      var(--silver-mid) 22%,
      var(--silver-light) 48%,
      var(--silver-mid) 72%,
      var(--silver-dark) 100%);
  }
  .address-band {
    position: absolute;
    top: 0; left: 0; right: 0;
    height: 140px;
    background: linear-gradient(180deg, var(--band-blue) 0%, var(--band-blue-dark) 100%);
    border-bottom: 5px solid var(--rule-white);
    display: flex;
    align-items: center;
    justify-content: center;
  }
  .address {
    font-family: "Cinzel", serif;
    font-weight: 400;
    font-size: 30px;
    line-height: 1.1;
    letter-spacing: 1.5px;
    color: var(--address-white);
    text-align: center;
    font-style: normal;
  }
  .brand {
    position: absolute;
    left: 0; right: 0;
    top: 230px;
    display: flex;
    align-items: center;
    justify-content: center;
    gap: 26px;
  }
  .brand-mark {
    width: 70px;
    height: 70px;
    flex: none;
  }
  .brand-name {
    font-family: "Cinzel", serif;
    font-weight: 600;
    font-size: 64px;
    letter-spacing: 2px;
    color: var(--ink-blue);
    white-space: nowrap;
  }
</style>
</head>
<body>
  <main class="canvas">
    <section class="business-card">
      <header class="address-band">
        <address class="address">
          4375 Calverton Road Mississauga,<br>
          ON L4W 2K7 Canada
        </address>
      </header>
      <div class="brand">
        <svg class="brand-mark" viewBox="0 0 70 70" aria-hidden="true">
          <circle cx="35" cy="35" r="33" fill="var(--ink-blue)"/>
        </svg>
        <span class="brand-name">Northgate Limited</span>
      </div>
    </section>
  </main>
</body>
</html>
```